National Chemical Line for Homeowners Needs a Logo & Label Design.

We need a logo and label design for a New National Chemical Company that is Private Labeling/Creating Cleaning Chemicals for Homeowners to use themselves. These chemicals will be used to clean carpets, hard surfaces, remove cat & dog stains and odors and many other products to come.
The first product will be for homeowners to remove cat & dog stains and odors from their carpets. We would like the label for the front and back of a 32 oz. white spray bottle. Go to www.brellowsupply.com and reference Part# 41KPL7.
We want the bottle/label to stand out on the grocery store shelves. We want it to be simple to read, eye catching, have a simple name and explain what the product does . The back of the bottle will have directions, caution statements, etc.
The Name of our Company is Tidal Marvels. It does have a trademark. We want the word "Tidal" to stand out and the word "marvels to only be present, that way the word Tidal will gain traction with the customer.
We want the color scheme to be Pinks & Blues.

```html
<!DOCTYPE html>
<html lang="en">
<head>
<meta charset="utf-8">
<title>Tidal Marvels – Pet Stain &amp; Odor Remover Label</title>
<link href="https://fonts.googleapis.com/css2?family=Poppins:wght@700;800&family=Outfit:wght@500&family=Oswald:wght@400&display=swap" rel="stylesheet">
<style>
  :root {
    --pink: #ff0a84;
    --pink-pale: #ffe8f3;
    --navy: #1f1a8f;
    --navy-deep: #24215f;
    --silver: #e4e4ea;
    --white: #ffffff;
    --text-blue: #1c1a9a;
  }
  * { margin: 0; padding: 0; box-sizing: border-box; }
  html, body {
    width: 1200px; height: 1198px; overflow: hidden; background: var(--white);
  }
  .label {
    position: absolute; left: 270px; top: 170px; width: 660px; height: 860px;
  }
  .label-shape { position: absolute; inset: 0; }
  .brand { position: absolute; top: 130px; left: 0; width: 100%; text-align: center; color: var(--white); }
  .brand-primary {
    display: block;
    font: 800 124px/1 "Poppins", sans-serif;
    letter-spacing: 2px;
  }
  .brand-secondary {
    display: block; margin-top: 4px;
    font: 800 30px/1 "Poppins", sans-serif;
    letter-spacing: 8px;
  }
  .product-badge {
    position: absolute; top: 352px; left: 80px; width: 500px; height: 250px;
    transform: rotate(-8deg);
  }
  .product-badge svg { position: absolute; inset: 0; }
  .product-title {
    position: absolute; top: 36px; left: 0; width: 100%;
    text-align: center;
    font: 700 40px/1.08 "Poppins", sans-serif;
    color: var(--white);
  }
  .product-use {
    position: absolute; top: 151px; left: 0; width: 100%;
    text-align: center;
    font: 700 23px/1.15 "Poppins", sans-serif;
    color: var(--navy-deep);
  }
  .benefits {
    position: absolute; top: 642px; left: 190px; list-style: none;
    font: 500 22px/1.55 "Outfit", sans-serif;
    color: var(--text-blue);
  }
  .benefits li { display: flex; align-items: center; gap: 12px; }
  .benefits svg { width: 20px; height: 20px; }
  .net-contents {
    position: absolute; top: 772px; left: 0; width: 100%;
    text-align: center;
    font: 400 26px/1 "Oswald", sans-serif;
    color: var(--pink);
    letter-spacing: 1px;
  }
</style>
</head>
<body>
<main class="label">
  <svg class="label-shape" viewBox="0 0 660 860" width="660" height="860">
    <defs>
      <linearGradient id="labelFill" x1="0" y1="0" x2="0" y2="1">
        <stop offset="0" stop-color="#ff0a84"/>
        <stop offset="0.5" stop-color="#ff0a84"/>
        <stop offset="1" stop-color="#ffe8f3"/>
      </linearGradient>
    </defs>
    <path d="M30,190 C90,70 250,20 380,30 C520,45 640,130 640,250 L630,780 Q625,840 560,845 L90,845 Q30,840 28,780 Z"
          fill="url(#labelFill)" stroke="#1f1a8f" stroke-width="9"/>
    <path d="M44,196 C100,86 252,38 380,46 C510,60 624,140 624,252 L614,776 Q610,826 556,830 L94,830 Q46,826 44,778 Z"
          fill="none" stroke="#ffffff" stroke-width="3" opacity="0.7"/>
  </svg>

  <div class="brand">
    <span class="brand-primary">Tidal</span>
    <span class="brand-secondary">MARVELS</span>
  </div>

  <div class="product-badge">
    <svg viewBox="0 0 500 250" width="500" height="250">
      <polygon points="70,5 430,5 495,115 430,245 70,245 5,115" fill="#24215f"/>
      <polygon points="30,136 470,136 455,220 45,220" fill="#e4e4ea"/>
    </svg>
    <div class="product-title">Pet Stain &amp;<br>Odor Remover</div>
    <div class="product-use">For Carpets and<br>Upholstery</div>
  </div>

  <ul class="benefits">
    <li><svg viewBox="0 0 20 20"><path d="M3,10 L8,15 L17,4" fill="none" stroke="#1c1a9a" stroke-width="3"/></svg>Removes Tough Pet Stains</li>
    <li><svg viewBox="0 0 20 20"><path d="M3,10 L8,15 L17,4" fill="none" stroke="#1c1a9a" stroke-width="3"/></svg>Neutralizes Odors</li>
    <li><svg viewBox="0 0 20 20"><path d="M3,10 L8,15 L17,4" fill="none" stroke="#1c1a9a" stroke-width="3"/></svg>Safe for Home Use</li>
  </ul>

  <div class="net-contents">32 fl oz (946 mL)</div>
</main>
</body>
</html>
```